I am looking for a design for my business card. I need a logo. The company is called Harborline Capital. We are an investment management and technology consulting company. I am looking for a professional conservative design. I think a lighthouse might be a good simple for us.

For the business card.
company URL www.harborlinecapital.example
my name: Philip R. Kessler
email: pkessler@harborlinecapital.example
my phone # 318-469-5730

Contact Information for Business Card

company URL www.harborlinecapital.example my name: Philip R. Kessler email: pkessler@harborlinecapital.example my phone # 318-469-5730

Colors
0054AA
0677BA
7BADD7
CADEEF
E8F1F8

Requirements
Must have
• area on the back for a QR code

```html
<!DOCTYPE html>
<html lang="en">
<head>
<meta charset="utf-8">
<title>Harborline Capital – Business Card</title>
<link href="https://fonts.googleapis.com/css2?family=Montserrat:wght@300;400;600&family=Oswald:wght@600&display=swap" rel="stylesheet">
<style>
  :root {
    --backdrop: #1c1c1c;
    --card-dark: #151515;
    --card-dark-glow: #262626;
    --card-light: #ffffff;
    --ink: #111111;
    --muted: #7a7a7a;
    --qr-zone: #f2f2f2;
    --qr-edge: #d9d9d9;
    --brand-blue: #2a7bc8;
    --brand-green: #2eaa48;
    --white: #ffffff;
  }
  * { margin: 0; padding: 0; box-sizing: border-box; }
  html, body {
    width: 1200px; height: 900px; overflow: hidden;
    background: var(--backdrop);
  }
  .sheet {
    width: 1200px; height: 900px;
    display: flex; flex-direction: column;
    align-items: center; justify-content: center;
    gap: 40px;
  }
  .card {
    width: 700px; height: 400px;
    border-radius: 26px;
    position: relative;
    overflow: hidden;
  }
  /* Front */
  .card--front {
    background: radial-gradient(ellipse at 55% 40%, var(--card-dark-glow), var(--card-dark) 70%);
    display: flex; align-items: center; justify-content: center;
  }
  .brand {
    display: flex; align-items: center; gap: 22px;
  }
  .brand__mark {
    width: 46px; height: 46px;
    background: var(--brand-blue);
  }
  .brand__name {
    font-family: "Montserrat", sans-serif;
    font-weight: 600;
    font-size: 36px;
    letter-spacing: 4px;
    text-transform: uppercase;
    color: var(--white);
    white-space: nowrap;
  }
  /* Back */
  .card--back {
    background: var(--card-light);
  }
  .identity {
    position: absolute;
    left: 44px; right: 36px; top: 150px;
    display: flex; align-items: center; gap: 22px;
  }
  .person {
    display: flex; flex-direction: column; align-items: flex-end;
    flex: none;
  }
  .person__name {
    font-family: "Oswald", sans-serif;
    font-weight: 600;
    font-size: 40px;
    line-height: 1.05;
    text-transform: uppercase;
    color: var(--ink);
    letter-spacing: 0.3px;
    white-space: nowrap;
  }
  .person__title {
    font-family: "Montserrat", sans-serif;
    font-weight: 400;
    font-size: 16px;
    color: var(--muted);
    margin-top: 2px;
    letter-spacing: 0.5px;
  }
  .divider {
    width: 2px; height: 80px;
    background: var(--brand-blue);
    flex: none;
  }
  .contacts {
    list-style: none;
    display: flex; flex-direction: column; gap: 6px;
    min-width: 0;
  }
  .contacts__item {
    display: flex; align-items: center; gap: 9px;
    font-family: "Montserrat", sans-serif;
    font-weight: 400;
    font-size: 13px;
    color: var(--muted);
    white-space: nowrap;
  }
  .contacts__icon {
    width: 15px; height: 15px; flex: none;
  }
  .qr-zone {
    position: absolute;
    right: 36px; bottom: 32px;
    width: 92px; height: 92px;
    background: var(--qr-zone);
    border: 1px solid var(--qr-edge);
    border-radius: 6px;
  }
</style>
</head>
<body>
<main class="sheet">
  <section class="card card--front" aria-label="Card front">
    <div class="brand">
      <span class="brand__mark"></span>
      <span class="brand__name">Harborline Capital</span>
    </div>
  </section>

  <section class="card card--back" aria-label="Card back">
    <div class="identity">
      <div class="person">
        <h1 class="person__name">Philip R. Kessler</h1>
        <p class="person__title">President</p>
      </div>
      <span class="divider"></span>
      <ul class="contacts">
        <li class="contacts__item">
          <svg class="contacts__icon" viewBox="0 0 16 16" aria-hidden="true">
            <path d="M3.2 1.5l2.4 2.8-1.3 1.9c.9 2 2.5 3.6 4.5 4.5l1.9-1.3 2.8 2.4-1.4 2.2C7.4 13.6 2.4 8.6 1 3.1z" fill="var(--brand-green)"/>
          </svg>
          318-469-5730
        </li>
        <li class="contacts__item">
          <svg class="contacts__icon" viewBox="0 0 16 16" aria-hidden="true">
            <rect x="1" y="3.5" width="14" height="9" fill="var(--brand-green)"/>
            <polyline points="1,3.5 8,9 15,3.5" fill="none" stroke="var(--white)" stroke-width="1.3"/>
          </svg>
          pkessler@harborlinecapital.example
        </li>
        <li class="contacts__item">
          <svg class="contacts__icon" viewBox="0 0 16 16" aria-hidden="true" fill="none" stroke="var(--brand-green)" stroke-width="1.4">
            <circle cx="8" cy="8" r="6.5"/>
            <ellipse cx="8" cy="8" rx="2.8" ry="6.5"/>
            <line x1="1.5" y1="8" x2="14.5" y2="8"/>
          </svg>
          www.harborlinecapital.example
        </li>
      </ul>
    </div>
    <div class="qr-zone" role="img" aria-label="Reserved area for QR code"></div>
  </section>
</main>
</body>
</html>
```